Buch-/eBook-Cover Das Lied der Salzmühlen
Lukas Brandmoor (malvorin) hat mich von Anfang an mit seiner Professionalität, Kreativität und Kommunikationsweise überzeugt. Er hat sich ausgezeichnet auf meine Vorstellungen eingelassen und die verschiedenen Entwürfe in gemeinsamer Arbeit weiterentwickelt, bis ein perfektes Resultat vorlag.
Zielgruppe
Ich bin Professor für Religionswissenschaft an der Universität Hallweide. Dieses Sachbuch zur Das Lied der Salzmühlen ist 2003 bei R.T.Wolm erschienen (2007 dann als Taschenbuch), die Rechte sind inzwischen an mich zurückgegangen. Die vollständig überarbeitete Neuauflage erscheint als Self-Publishing (PressaLuma), wobei ich als Herausgeber einen von mir gegründeten ThinkTank (Brightfold: Weaving Insight) verwende. Das Sachbuch richtet sich an alle, die an der Astrologie interessiert sind. Mit der Neuauflage möchte ich insbesondere auch ein jüngeres Publikum ansprechen.
Aufgabenstellung
Ich brauche ein Cover mit konkreten Maßen, die ich als ein Template von PressaLuma bekommen habe (plus ein 'abgespecktes' für das eBook). Das Cover sollte sich von dem Cover der Erstpublikation unterscheiden und moderner daherkommen, um auch ein jüngeres Publikum anzusprechen. Auf der Vorderseite sollte der Autorenname (Dörte von Halmsee), der Titel (Das Lied der verlorenen Salzmühlen) und Untertitel (Vom Flussufer bis zum Leuchtturm) sowie unten der Herausgeber (Brightfold: Weaving Insight; evt. auch nur Brightfold).
Auf der Rückseite sollten Zitate von Rezensionen aufgenommen werden (s. Datei). Unten rechts muss Platz frei bleiben für die ISBN (s. Template von PressaLuma).
Im Buch selber gibt es Abbildungen (frei verfügbar), die man evt. auch für das Cover verwenden/anpassen könnte. S. dazu die Dateien, die ich mit hochlade. Andere Abbildungen können natürlich auch verwendet werden.
Das Design darf nicht zu überladen sein.

```html
<!DOCTYPE html>
<html lang="de">
<head>
<meta charset="utf-8">
<title>Das Lied der verlorenen Salzmühlen – Cover</title>
<link href="https://fonts.googleapis.com/css2?family=Source+Serif+4:wght@400;500;600&family=Inter:ital,wght@0,400;1,400&display=swap" rel="stylesheet">
<style>
  :root {
    --navy-deep: #0f2440;
    --navy-mid: #1c3556;
    --charcoal: #2b2b2d;
    --gold: #c9a96c;
    --gold-soft: #b8925c;
    --ink-light: #f3f0ea;
    --paper: #f1efea;
    --ink-dark: #2a2a2a;
    --ink-grey: #4a4a4a;
    --sphere-blue: #4f74a6;
    --sphere-copper: #a7744a;
  }
  * { margin: 0; padding: 0; box-sizing: border-box; }
  html, body { width: 1182px; height: 1200px; overflow: hidden; background: var(--paper); }
  .cover { position: relative; width: 1182px; height: 1200px; }

  .spine {
    position: absolute; left: 0; top: 0; width: 46px; height: 1200px;
    background: linear-gradient(180deg, var(--navy-deep) 0%, #152a47 60%, #1b2230 100%);
    color: var(--ink-light);
    display: flex; flex-direction: column; align-items: center;
    padding: 26px 0 30px;
  }
  .spine-text {
    writing-mode: vertical-rl;
    font-family: "Source Serif 4", serif;
    font-size: 23px; white-space: nowrap;
  }
  .spine-author { margin-bottom: 22px; }
  .spine-publisher { margin-top: auto; font-family: "Inter", sans-serif; font-size: 16px; }

  .front {
    position: absolute; left: 46px; top: 0; width: 693px; height: 1200px;
    background: linear-gradient(180deg, var(--navy-deep) 0%, var(--navy-mid) 45%, #24324a 70%, var(--charcoal) 100%);
    text-align: center; color: var(--ink-light);
    font-family: "Source Serif 4", serif;
  }
  .front-art {
    position: absolute; left: 30px; top: 250px; width: 633px; height: 640px;
    border-radius: 50%;
    background:
      radial-gradient(ellipse 48% 22% at 50% 52%, rgba(167,116,74,0.55) 0%, rgba(167,116,74,0.15) 70%, transparent 100%),
      radial-gradient(circle at 50% 40%, rgba(79,116,166,0.55) 0%, rgba(79,116,166,0.18) 45%, transparent 70%);
  }
  .author { position: absolute; top: 92px; width: 100%; font-size: 35px; font-weight: 400; }
  .title {
    position: absolute; top: 196px; width: 100%;
    font-size: 53px; line-height: 60px; font-weight: 500; color: var(--gold);
  }
  .keyword {
    position: absolute; top: 878px; width: 100%;
    font-size: 74px; font-weight: 500; color: var(--gold);
  }
  .subtitle {
    position: absolute; top: 968px; width: 100%;
    font-size: 35px; line-height: 42px; font-weight: 400;
  }
  .publisher {
    position: absolute; top: 1108px; width: 100%;
    font-family: "Inter", sans-serif; font-size: 17px; color: #d6d3cc;
  }

  .back {
    position: absolute; left: 739px; top: 0; width: 443px; height: 1200px;
    background: var(--paper); padding: 92px 40px 0 44px; color: var(--ink-dark);
  }
  .back-title {
    font-family: "Source Serif 4", serif; font-weight: 400;
    font-size: 30px; line-height: 38px; color: var(--ink-grey); margin-bottom: 40px;
  }
  .review { font-family: "Inter", sans-serif; font-size: 18.5px; line-height: 24px; margin-bottom: 32px; }
  .review-source { font-style: italic; }
  .ref { font-style: normal; font-size: 9px; vertical-align: super; color: #666; }
</style>
</head>
<body>
<div class="cover">
  <aside class="spine">
    <span class="spine-text spine-author">Dörte von Halmsee</span>
    <span class="spine-text spine-title">Das Lied der verlorenen Salzmühlen</span>
    <span class="spine-text spine-publisher">Brightfold</span>
  </aside>

  <section class="front">
    <div class="front-art" role="img" aria-label="Illustration einer Armillarsphäre mit kupferfarbenem Ring und Tierkreiszeichen auf nachtblauem Grund"></div>
    <p class="author">Dörte von Halmsee</p>
    <h1 class="title">Das Lied der<br>verlorenen<br>Salzmühlen</h1>
    <p class="keyword">Asstrologie</p>
    <p class="subtitle">Vom Flussufer<br>bis zum Leuchtturm</p>
    <p class="publisher">Brightfold: Weaving Insight</p>
  </section>

  <section class="back">
    <h2 class="back-title">Das Lied der<br>verlorenen Salzmühlen</h2>
    <p class="review">„Von Halmsee hat die gut 3000-jährige Geschichte der Astrologie souverän nachgezeichnet und damit … neue Maßstäbe für die kulturhistorische Analyse der Astrologie gesetzt.“<br>– <span class="review-source">Nordufer Rundschau</span> <span class="ref">[cite: 33, 34]</span></p>
    <p class="review">„Was die Astrologie spannend macht, ist ihre herausragende Rolle in der europäischen Kultur, und von dieser handelt das gut zu lesende und materialreiche Buch.“<br>– <span class="review-source">Lesezeichen</span> <span class="ref">[cite: 35, 36]</span></p>
    <p class="review">„Eine erstklassige Übersicht!“ – <span class="review-source">Blickpunkt</span> <span class="ref">37, 38]</span></p>
    <p class="review">„Das einfühlsame Buch … ist eine gute Einführung in die Geschichte einer uralten Kulturtechnik und gibt Einblick in die astrologische Mentalität.“<br>– <span class="review-source">Südländer Tagblatt</span> <span class="ref">[cite: 39, 40]</span></p>
  </section>
</div>
</body>
</html>
```